RVM Flooring Flyer/Direct Mail

I need a flyer that will be distributed by letterboxing. this flyer will be offering free measure and quotes for supply and installation of timber, bamboo, and laminate flooring. The flyer will need to eye catching and professional looking.
The main purpose of the flyer is to generate appointments that will be followed up by a sales measure and quote team.

- Free Measure and Quote
Services:
- Remove and dispose of old floor coverings
- Pre installation floor repair
- New floor installation
- Free dust and clean on every new floor installation

I have some design files, logo and stock images, the flyer must not clash with the logo and business card.

You can use any image from Pextra Images as I have subscription with them.
https://images.pextrafoto.com/au/gallery

Here are the links to the Timber and Bamboo flooring supplier that I will be buying from and the third link is for the laminate flooring supplier. Note, this is for getting an idea of what products we will be supplying and installing, Do not use their images!

https://www.grainhaven.com.au/timber-flooring/
https://cantorvex.com.au/bamboo-flooring/
http://www.dalvorsurfaces.com.au/brands/tenmark-laminate/

Target Market(s)

Domestic home owners

Industry/Entity Type

Construction Company

Colors

Designer to choose colors to be used in the design.

Requirements
Must have
• Size: A6 or DL
Nice to have
• Timber: Spotted Gum, Eastern States Blackbutt, Jarrah, Marri, and a large collection of French Oak.
• Bamboo: Our Bamboo range of flooring is engineered to withstand the extremes of the Australian climate.
• Laminate: All our laminate range comes with a 25 year product warranty. Choose from a large range of patterns, colours and finishes.

```html
<!DOCTYPE html>
<html lang="en">
<head>
<meta charset="utf-8">
<title>RVM Flooring Flyer / Direct Mail</title>
<link rel="stylesheet" href="https://fonts.googleapis.com/css2?family=Montserrat:wght@400;600;800&family=Oswald:wght@300;400;500;700&family=Cinzel:wght@400&display=swap">
<style>
:root{
  --ink:#1c2229;
  --board-top:#d9d9d9;
  --board-bottom:#b9b9b9;
  --dark:#161616;
  --mid:#6d6d6d;
  --silver:#d4d4d4;
  --muted:#8e8e8e;
  --white:#ffffff;
}
*{margin:0;padding:0;box-sizing:border-box}
html,body{width:1200px;height:1096px;overflow:hidden}
body{position:relative;background:linear-gradient(180deg,var(--board-top),var(--board-bottom));font-family:'Montserrat',sans-serif;color:var(--ink)}
.board-header{position:absolute;left:0;top:0;width:1200px;height:130px;background:var(--ink);color:var(--white)}
.board-title{position:absolute;left:56px;top:40px;font-weight:800;font-size:44px;letter-spacing:.5px}
.board-size{position:absolute;right:78px;top:52px;font-size:25px;font-weight:400}
.side-label{position:absolute;font-size:25px;font-weight:400;letter-spacing:.5px;color:#111}
.side-label.front{left:242px;top:205px}
.side-label.back{left:801px;top:210px}
.flyer{position:absolute;top:257px;width:528px;height:744px;overflow:hidden;box-shadow:4px 6px 14px rgba(0,0,0,.35)}
.flyer.front{left:54px;background:linear-gradient(180deg,#fafafa,#e4e4e4)}
.flyer.back{left:610px;background:linear-gradient(180deg,#2b2b2b,#111 70%)}
.abs{position:absolute}
.brand{font-family:'Montserrat',sans-serif;font-weight:600;color:var(--silver);letter-spacing:1px;white-space:nowrap}
.brand.hero{left:288px;top:140px;font-size:23px}
.product-circle{position:absolute;border-radius:50%;border:8px solid var(--white);box-shadow:0 3px 8px rgba(0,0,0,.35)}
.ribbon{position:absolute;top:0;left:0}
.ribbon-label{position:absolute;font-family:'Oswald',sans-serif;font-weight:500;color:var(--silver);text-align:center;letter-spacing:.5px;border-bottom:2px dotted #666;padding-bottom:4px;white-space:nowrap}
.intro-title{left:32px;top:528px;font-size:27px;font-weight:600;color:#222}
.intro-copy{left:32px;top:570px;width:290px;font-family:'Oswald',sans-serif;font-weight:300;font-size:11px;line-height:14.6px;color:#333;text-align:justify}
.intro-copy b{font-weight:500}
.offer{position:absolute;text-align:center;font-family:'Oswald',sans-serif;white-space:nowrap}
.offer .line1{display:block;font-weight:500;line-height:1}
.offer .line2{display:block;font-weight:700;line-height:1}
.offer .cta{display:block;border:2px solid currentColor;font-weight:400;text-transform:uppercase}
.offer.front-offer{left:347px;top:532px;width:150px;color:#222}
.front-offer .line1{font-size:24px;color:#666;letter-spacing:-.3px}
.front-offer .line2{font-size:31px;margin-top:2px;letter-spacing:-.3px}
.front-offer .cta{margin-top:7px;font-size:12px;line-height:15px;padding:3px 0;border-color:#333}
.front-note{left:340px;top:646px;width:164px;text-align:center;font-family:'Oswald',sans-serif;font-weight:300;font-size:9.5px;color:#333;white-space:nowrap}
.footer{left:0;bottom:0;width:528px;height:75px}
.footer .brand{position:absolute;left:66px;top:30px;font-size:13px}
.footer-dot{position:absolute;left:32px;top:23px;width:26px;height:26px;border-radius:50%;border:2px solid var(--silver)}
.contact{position:absolute;top:22px;font-size:10px;line-height:13px;color:var(--white);white-space:nowrap}
.contact .head{font-weight:600;font-size:11.5px}
.contact.addr{left:240px}
.contact.reach{left:366px}
.contact svg{width:8px;height:8px;margin-right:4px;vertical-align:-1px;fill:var(--white)}
.brand.back-brand{left:0;width:528px;text-align:center;top:402px;font-size:26px}
.services-title{left:36px;top:470px;color:var(--white);font-size:29px;white-space:nowrap}
.services-title .serif{font-family:'Cinzel',serif;font-weight:400}
.services-title .bold{font-weight:600}
.services{left:36px;top:522px;list-style:none;font-family:'Oswald',sans-serif;font-weight:300;font-size:15.5px;color:var(--white);line-height:20px}
.services li{position:relative;padding-left:22px;margin-bottom:7px;white-space:nowrap}
.services li::before{content:"";position:absolute;left:1px;top:6px;width:9px;height:9px;border-radius:50%;border:1.5px solid var(--silver)}
.offer.back-offer{left:308px;top:484px;width:188px;color:var(--white)}
.back-offer .line1{font-size:30px;color:var(--muted);letter-spacing:-.3px}
.back-offer .line2{font-size:38px;margin-top:2px;letter-spacing:-.3px}
.back-offer .cta{margin-top:7px;font-size:15px;line-height:18px;padding:4px 0}
.back-phone{left:310px;top:612px;font-family:'Oswald',sans-serif;font-weight:500;font-size:28px;line-height:36px;color:var(--white);white-space:nowrap}
.back-phone svg{width:16px;height:26px;vertical-align:-3px;margin-right:6px}
</style>
</head>
<body>
<header class="board-header">
  <div class="board-title">RVM FLOORING FLYER/DIRECT MAIL</div>
  <div class="board-size">A6 SIZE</div>
</header>

<div class="side-label front">FLYER FRONT</div>
<div class="side-label back">FLYER BACK</div>

<section class="flyer front">
  <svg class="abs" style="left:0;top:290px" width="528" height="380" role="img" aria-label="Faint bright living room interior behind the text">
    <defs><linearGradient id="roomFaint" x1="0" y1="0" x2="0" y2="1"><stop offset="0" stop-color="#f7f7f7"/><stop offset="1" stop-color="#dcdcdc"/></linearGradient></defs>
    <rect width="528" height="380" fill="url(#roomFaint)"/>
  </svg>
  <svg class="abs" style="left:0;top:0" width="528" height="270" role="img" aria-label="Dark backdrop with stacked timber floorboard samples">
    <defs><linearGradient id="planks" x1="0" y1="0" x2="1" y2="1"><stop offset="0" stop-color="#7a5a44"/><stop offset=".35" stop-color="#4a3a33"/><stop offset=".6" stop-color="#242424"/><stop offset="1" stop-color="#111"/></linearGradient></defs>
    <polygon points="0,0 528,0 528,268 440,232 40,232 0,255" fill="url(#planks)"/>
    <polygon points="40,232 440,232 528,268 528,270 0,270 0,255" fill="#0d0d0d"/>
  </svg>
  <div class="abs brand hero">RVM FLOORING</div>

  <svg class="ribbon" width="528" height="520">
    <polygon points="46,260 170,260 170,487 108,458 46,487" fill="#1e1e1e" stroke="#555" stroke-width="2"/>
    <polygon points="360,260 483,260 483,487 421,458 360,487" fill="#1e1e1e" stroke="#555" stroke-width="2"/>
    <polygon points="184,260 345,260 345,515 264,482 184,515" fill="#1a1a1a" stroke="#555" stroke-width="2"/>
  </svg>
  <div class="ribbon-label" style="left:74px;top:408px;width:70px;font-size:21px">TIMBER</div>
  <div class="ribbon-label" style="left:216px;top:425px;width:96px;font-size:25px">BAMBOO</div>
  <div class="ribbon-label" style="left:378px;top:410px;width:88px;font-size:20px">LAMINATE</div>

  <div class="product-circle" role="img" aria-label="Close-up of timber flooring" style="left:26px;top:211px;width:160px;height:160px;background:linear-gradient(135deg,#8a3e22,#c9a57d 45%,#e7d4b4)"></div>
  <div class="product-circle" role="img" aria-label="Close-up of bamboo flooring" style="left:169px;top:200px;width:188px;height:188px;background:linear-gradient(120deg,#c98a2e,#e0a94b 50%,#b77a25)"></div>
  <div class="product-circle" role="img" aria-label="Close-up of laminate flooring" style="left:349px;top:215px;width:152px;height:152px;background:linear-gradient(160deg,#7a5238,#b98a62 50%,#8e6446)"></div>

  <div class="abs brand intro-title">RVM FLOORING</div>
  <p class="abs intro-copy">At <b>RVM flooring</b> we specialise in prefinished timber, bamboo and laminate flooring. We strive to provide a unique and professional experience to all our customers. Our goal is to provide the highest standard in customer service, integrity, quality and value for money. As a family business we understand the importance of relationship and seek to make your experience one you will be pleased you made.</p>

  <div class="offer front-offer">
    <span class="line1">FREE MEASURE</span>
    <span class="line2">AND QUOTE</span>
    <span class="cta">Call today for your<br>obligations free quote</span>
  </div>
  <div class="abs front-note">Call us today to view our range of products</div>

  <footer class="abs footer">
    <svg class="abs" width="528" height="75"><polygon points="0,0 176,0 222,75 0,75" fill="#1b1b1b"/><polygon points="176,0 528,0 528,75 222,75" fill="var(--mid)"/></svg>
    <div class="footer-dot"></div>
    <div class="brand">RVM FLOORING</div>
    <div class="contact addr"><span class="head"><svg viewBox="0 0 10 10"><path d="M5 0a3.5 3.5 0 0 1 3.5 3.5C8.5 6 5 10 5 10S1.5 6 1.5 3.5A3.5 3.5 0 0 1 5 0z"/></svg>Address:</span><br>47 Kestrel Avenue<br>Marlow WA 6091</div>
    <div class="contact reach"><svg viewBox="0 0 10 10"><rect x="2.5" y="0" width="5" height="10" rx="1"/></svg>0400 118 272<br><svg viewBox="0 0 10 10"><path d="M2 0l2 2-1 2c1 1.5 2 2.5 3 3l2-1 2 2-2 2C4 9 1 6 0 2z"/></svg>08 9000 4417<br><svg viewBox="0 0 10 10"><rect x="0" y="2" width="10" height="6"/></svg>Sam@RVMFlooring.com.au</div>
  </footer>
</section>

<section class="flyer back">
  <svg class="abs" style="left:0;top:0" width="528" height="372" role="img" aria-label="Modern dining room interior with pendant lights, concrete wall and fireplace">
    <defs><linearGradient id="room" x1="0" y1="0" x2="0" y2="1"><stop offset="0" stop-color="#e6e6e6"/><stop offset=".55" stop-color="#9d9d9d"/><stop offset="1" stop-color="#c9c9c9"/></linearGradient></defs>
    <polygon points="0,0 528,0 528,258 264,345 0,258" fill="url(#room)"/>
    <polygon points="0,258 264,345 528,258 528,285 264,372 0,285" fill="#3a3a3a"/>
  </svg>
  <div class="abs brand back-brand">RVM FLOORING</div>

  <div class="abs services-title"><span class="serif">OUR</span> <span class="bold">SERVICES</span></div>
  <ul class="abs services">
    <li>Remove and dispose of old floor coverings</li>
    <li>Pre installation floor repair</li>
    <li>New floor installation</li>
    <li>Free dust and clean on every new<br>floor installation</li>
  </ul>

  <div class="offer back-offer">
    <span class="line1">FREE MEASURE</span>
    <span class="line2">AND QUOTE</span>
    <span class="cta">Call today for your<br>obligations free quote</span>
  </div>
  <div class="abs back-phone"><svg viewBox="0 0 20 32"><rect x="2" y="2" width="16" height="28" rx="2" fill="none" stroke="#fff" stroke-width="2.5"/><rect x="8" y="25" width="4" height="2" fill="#fff"/></svg>0400 118 272</div>

  <footer class="abs footer">
    <svg class="abs" width="528" height="75"><polygon points="0,0 200,0 240,75 0,75" fill="#1b1b1b"/><polygon points="200,0 528,0 528,75 240,75" fill="var(--mid)"/></svg>
    <div class="footer-dot"></div>
    <div class="brand">RVM FLOORING</div>
    <div class="contact addr"><span class="head"><svg viewBox="0 0 10 10"><path d="M5 0a3.5 3.5 0 0 1 3.5 3.5C8.5 6 5 10 5 10S1.5 6 1.5 3.5A3.5 3.5 0 0 1 5 0z"/></svg>Address:</span><br>47 Kestrel Avenue<br>Marlow WA 6091</div>
    <div class="contact reach"><svg viewBox="0 0 10 10"><rect x="2.5" y="0" width="5" height="10" rx="1"/></svg>0400 118 272<br><svg viewBox="0 0 10 10"><path d="M2 0l2 2-1 2c1 1.5 2 2.5 3 3l2-1 2 2-2 2C4 9 1 6 0 2z"/></svg>08 9000 4417<br><svg viewBox="0 0 10 10"><rect x="0" y="2" width="10" height="6"/></svg>Sam@RVMFlooring.com.au</div>
  </footer>
</section>
</body>
</html>
```